NEW APP LAUNCH FOR HEALTHY CONCEPT RESTAURANT

We are looking for a design to post on our social media outlets, instagram and facebook to introduce our new app launch! We are looking for maybe a phone in the graphic, along with a catchy phrase or something along those lines. This app will manage customer accounts, and they can order take out, meal prep and delivery orders all through the app.

Target Market(s)

Ages 25-35 in Alberta Canada

```html
<!DOCTYPE html>
<html lang="en">
<head>
<meta charset="utf-8">
<title>Nourish – App Launch Posts</title>
<link href="https://fonts.googleapis.com/css2?family=Lexend:wght@500;600;700&family=Montserrat:wght@500&family=Oswald:wght@500&display=swap" rel="stylesheet">
<style>
  :root{
    --green:#8cc63f;
    --grey:#8a8a8a;
    --ink:#111111;
    --page:#ffffff;
    --photo-green:#6f9c45;
    --photo-warm:#c9a27a;
    --photo-red:#9a3a4a;
    --photo-light:#eef0ea;
  }
  *{box-sizing:border-box;margin:0;padding:0}
  html,body{width:849px;height:1200px;overflow:hidden;background:var(--page)}
  .sheet{position:relative;width:849px;height:1200px;background:var(--page)}
  .post{position:absolute;left:88px;width:672px;background:var(--page);overflow:hidden;box-shadow:0 6px 24px rgba(0,0,0,.08)}
  .post--square{top:54px;height:672px}
  .post--wide{top:771px;height:352px}

  .photo{position:absolute}
  .post--square .photo{left:0;top:176px;width:466px;height:496px;
    background:
      linear-gradient(90deg,rgba(255,255,255,0) 55%,#fff 100%),
      linear-gradient(0deg,rgba(255,255,255,0) 70%,#fff 100%),
      radial-gradient(ellipse at 20% 40%,var(--photo-red) 0,transparent 30%),
      radial-gradient(ellipse at 65% 85%,var(--photo-warm) 0,transparent 45%),
      linear-gradient(160deg,var(--photo-green) 0%,#a9b88a 45%,#d9c7ae 100%);}
  .post--wide .photo{left:0;top:0;width:440px;height:352px;
    background:
      linear-gradient(90deg,rgba(255,255,255,0) 60%,#fff 100%),
      radial-gradient(ellipse at 15% 20%,var(--photo-red) 0,transparent 25%),
      radial-gradient(ellipse at 20% 55%,#c48a4a 0,transparent 30%),
      radial-gradient(ellipse at 70% 80%,var(--photo-warm) 0,transparent 45%),
      linear-gradient(160deg,#9bb07a 0%,var(--photo-light) 50%,#d8b99a 100%);}

  .brand{position:absolute;text-align:right;font-family:"Lexend",sans-serif;color:var(--green);white-space:nowrap}
  .brand__name{display:block;font-weight:700;line-height:1;letter-spacing:.02em}
  .brand__tagline{display:block;font-weight:700;line-height:1;letter-spacing:-.01em}
  .post--square .brand{right:36px;top:64px}
  .post--square .brand__name{font-size:64px}
  .post--square .brand__tagline{font-size:21px;margin-top:6px}
  .post--wide .brand{right:36px;top:36px}
  .post--wide .brand__name{font-size:40px}
  .post--wide .brand__tagline{font-size:13.5px;margin-top:4px}

  .headline{position:absolute;font-family:"Lexend",sans-serif;font-weight:600;color:var(--green);line-height:1.15;letter-spacing:-.015em;white-space:nowrap}
  .body-copy{position:absolute;font-family:"Montserrat",sans-serif;font-weight:500;color:var(--grey)}
  .post--square .headline{left:359px;top:308px;font-size:28px}
  .post--square .body-copy{left:359px;top:394px;width:292px;font-size:14px;line-height:19px}
  .post--wide .headline{left:392px;top:140px;font-size:24px}
  .post--wide .body-copy{left:392px;top:200px;width:262px;font-size:12px;line-height:15.5px}

  .stores{position:absolute;display:flex}
  .store{display:flex;align-items:center;background:var(--ink);color:#fff;border:1px solid #999;border-radius:5px;font-family:"Lexend",sans-serif;white-space:nowrap}
  .store__icon{background:#fff;border-radius:3px;flex:none}
  .store__text small{display:block;font-size:.42em;letter-spacing:.04em;line-height:1}
  .store__text b{display:block;font-weight:500;line-height:1.05}
  .post--square .stores{left:363px;top:571px;gap:12px}
  .post--square .store{width:108px;height:31px;padding:0 8px;gap:8px;font-size:14px}
  .post--square .store__icon{width:16px;height:16px}
  .post--wide .stores{left:395px;top:299px;gap:10px}
  .post--wide .store{width:98px;height:29px;padding:0 7px;gap:7px;font-size:13px}
  .post--wide .store__icon{width:15px;height:15px}

  .phone{position:absolute;width:189px;height:383px;border:6px solid var(--ink);border-radius:30px;background:#fff;overflow:hidden;transform-origin:0 0}
  .post--square .phone{left:114px;top:207px}
  .post--wide .phone{left:90px;top:64px;transform:scale(.67)}
  .phone__notch{position:absolute;left:44px;top:0;width:90px;height:12px;background:var(--ink);border-radius:0 0 10px 10px}
  .phone__header{position:absolute;left:0;top:0;width:100%;height:45px;border-bottom:1px solid #e6e6e6;padding:20px 0 0 20px;font-family:"Lexend",sans-serif;color:var(--green)}
  .phone__brand{font-weight:700;font-size:12px;line-height:1}
  .phone__tag{font-weight:700;font-size:4px;line-height:1;margin-top:1px;white-space:nowrap}
  .phone__menu{position:absolute;right:14px;top:21px;width:12px;height:9px;border-top:1px solid var(--green);border-bottom:1px solid var(--green)}
  .phone__menu::after{content:"";position:absolute;left:0;top:3px;width:100%;border-top:1px solid var(--green)}
  .tile{position:absolute;left:25px;width:127px;display:flex;align-items:center;justify-content:center;font-family:"Oswald",sans-serif;font-weight:500;color:#fff;font-size:20px;letter-spacing:.02em;white-space:nowrap}
  .tile--takeout{top:50px;height:133px;background:linear-gradient(160deg,#5b5b5b,#2f2f2f 60%,#8a7a66)}
  .tile--mealprep{top:202px;height:136px;background:linear-gradient(160deg,#3a4a36,#6e7b5b 45%,#2a2a2a)}
  .phone__top{position:absolute;left:146px;top:339px;width:18px;height:18px;border-radius:50%;background:#e3e3e3;display:flex;align-items:center;justify-content:center}
</style>
</head>
<body>
<main class="sheet">

  <section class="post post--square">
    <div class="photo" role="img" aria-label="Hand holding a phone over a table of fresh vegetables, beets and a grilled prawn salad"></div>
    <div class="phone">
      <div class="phone__notch"></div>
      <header class="phone__header">
        <div class="phone__brand">NOURISH</div>
        <div class="phone__tag">HEALTHY KITCHEN | MEAL PREP</div>
        <span class="phone__menu"></span>
      </header>
      <div class="tile tile--takeout" role="img" aria-label="Staff member holding a paper take-out bag">TAKE OUT</div>
      <div class="tile tile--mealprep" role="img" aria-label="Gloved hand garnishing meal prep containers">MEAL PREP</div>
      <span class="phone__top"><svg width="8" height="5" viewBox="0 0 8 5"><path d="M1 4 4 1 7 4" fill="none" stroke="#333" stroke-width="1.2"/></svg></span>
    </div>
    <div class="brand">
      <span class="brand__name">NOURISH</span>
      <span class="brand__tagline">HEALTHY KITCHEN | MEAL PREP</span>
    </div>
    <h1 class="headline">A healthier lifestyle<br>is one app away</h1>
    <p class="body-copy">Manage your accounts, order take out, meal prep and delivery orders all through one app</p>
    <div class="stores">
      <span class="store"><span class="store__icon"></span><span class="store__text"><small>GET IT ON</small><b>PlayHub</b></span></span>
      <span class="store"><span class="store__icon"></span><span class="store__text"><small>Available on the</small><b>AppDock</b></span></span>
    </div>
  </section>

  <section class="post post--wide">
    <div class="photo" role="img" aria-label="Hand holding a phone above bowls of salad, lentils and a prawn pasta dish"></div>
    <div class="phone">
      <div class="phone__notch"></div>
      <header class="phone__header">
        <div class="phone__brand">NOURISH</div>
        <div class="phone__tag">HEALTHY KITCHEN | MEAL PREP</div>
        <span class="phone__menu"></span>
      </header>
      <div class="tile tile--takeout" role="img" aria-label="Staff member holding a paper take-out bag">TAKE OUT</div>
      <div class="tile tile--mealprep" role="img" aria-label="Gloved hand garnishing meal prep containers">MEAL PREP</div>
      <span class="phone__top"><svg width="8" height="5" viewBox="0 0 8 5"><path d="M1 4 4 1 7 4" fill="none" stroke="#333" stroke-width="1.2"/></svg></span>
    </div>
    <div class="brand">
      <span class="brand__name">NOURISH</span>
      <span class="brand__tagline">HEALTHY KITCHEN | MEAL PREP</span>
    </div>
    <h2 class="headline">A healthier lifestyle<br>is one app away</h2>
    <p class="body-copy">Manage your accounts, order take out, meal prep and delivery orders all through one app</p>
    <div class="stores">
      <span class="store"><span class="store__icon"></span><span class="store__text"><small>GET IT ON</small><b>PlayHub</b></span></span>
      <span class="store"><span class="store__icon"></span><span class="store__text"><small>Available on the</small><b>AppDock</b></span></span>
    </div>
  </section>

</main>
</body>
</html>
```